Business Card Design Project

I need some business cards with the logo you did for us (attached)
I am looking for a coulourful yet serious business card

We do market research
on the back I want the logo

on the front my name : Corinne Valdessac
position : Manager
address : Brume Analytica Sarl - 27 Rue des tanneurs
1847 Glarency - Switzerland
corinne.valdessac@brumeanalytica.ch
Tel : +4122 934 07 58
Mob France :+33 671 42 8356
Mob Italy +39 347 520 8163

The tree of the logo could also be used alone

THE BACKGROUND COLOR ON THE FRONT HAS TO BE WHITE, ON THE BACK YU CAN TRY OHER COLOUR BUT HOMOGENEOUS (NOT EXPENSIVE TO PRINT)

Target Market(s)

multinational companies or other market research companies

Industry/Entity Type

Market Research

Requirements
Must have
• logo on the back
and all the info above

```html
<!DOCTYPE html>
<html lang="en">
<head>
<meta charset="utf-8">
<title>Brume Analytica – Business Card</title>
<link href="https://fonts.googleapis.com/css2?family=Fira+Sans:ital,wght@0,400;0,500;1,400&display=swap" rel="stylesheet">
<style>
  :root {
    --page: #ffffff;
    --card-white: #ffffff;
    --espresso: #2a0905;
    --band-dark: #2a0a05;
    --band-light: #6e3d31;
    --ink: #111111;
    --ink-soft: #555555;
    --emblem-tone: #e9dfe0;
    --shadow: 0 2px 6px rgba(0,0,0,.28);
  }
  html, body {
    margin: 0;
    padding: 0;
    width: 1200px;
    height: 670px;
    overflow: hidden;
    background: var(--page);
    font-family: "Fira Sans", sans-serif;
  }
  .canvas { position: relative; width: 1200px; height: 670px; }

  .card { position: absolute; box-shadow: var(--shadow); overflow: hidden; }

  /* Front */
  .card--front {
    left: 32px; top: 32px; width: 542px; height: 350px;
    background: var(--card-white);
  }
  .band {
    position: absolute;
    height: 15px;
    background: linear-gradient(90deg, var(--band-light), var(--band-dark) 45%);
  }
  .band--top { top: 0; left: 269px; right: 0; border-bottom-left-radius: 12px; }
  .band--bottom { bottom: 0; left: 19px; right: 0; border-top-left-radius: 12px; }

  .company { position: absolute; left: 18px; top: 44px; }
  .company__name { margin: 0; font-size: 23px; font-weight: 400; color: var(--ink); }
  .company__address {
    margin: 4px 0 0; font-size: 14px; font-style: italic;
    color: var(--ink-soft); line-height: 21px;
  }

  .emblem { position: absolute; left: 22px; top: 138px; }

  .contact { position: absolute; left: 273px; top: 157px; }
  .contact__name { margin: 0; font-size: 21px; font-weight: 400; color: var(--ink); }
  .contact__role { margin: 2px 0 0; font-size: 15px; color: var(--ink-soft); }
  .contact__email { margin: 16px 0 0; font-size: 14px; font-style: italic; color: var(--ink); }
  .phones { margin: 14px 0 0; border-collapse: collapse; font-size: 14px; font-style: italic; }
  .phones th {
    text-align: left; font-weight: 400;
    color: var(--ink-soft); width: 87px; padding: 0; height: 21.5px;
  }
  .phones td { padding: 0; color: var(--ink); }

  /* Back */
  .card--back {
    left: 626px; top: 286px; width: 543px; height: 352px;
    background: var(--espresso);
  }
  .back-panel {
    position: absolute; left: 70px; top: 52px; width: 401px; height: 247px;
    background: var(--card-white); border-radius: 14px;
    display: flex; align-items: center; justify-content: center; gap: 12px;
  }
  .brand-mark { width: 16px; height: 16px; background: var(--ink); }
  .brand-name { font-size: 34px; font-weight: 400; color: var(--ink); }
</style>
</head>
<body>
<main class="canvas">
  <section class="card card--front" aria-label="Business card front">
    <div class="band band--top"></div>

    <header class="company">
      <h1 class="company__name">Brume Analytica Sarl</h1>
      <p class="company__address">Address: 27 Rue des tanneurs<br>1847 Glarency, Switzerland</p>
    </header>

    <svg class="emblem" width="180" height="190" viewBox="0 0 180 190" role="img" aria-label="Company emblem illustration area">
      <rect x="0" y="0" width="180" height="190" rx="20" fill="var(--emblem-tone)"/>
    </svg>

    <div class="contact">
      <h2 class="contact__name">Corinne Valdessac</h2>
      <p class="contact__role">Manager</p>
      <p class="contact__email">corinne.valdessac@brumeanalytica.ch</p>
      <table class="phones">
        <tr><th>Telephone:</th><td>+4122 934 07 58</td></tr>
        <tr><th>Mob France:</th><td>+33 671 42 8356</td></tr>
        <tr><th>Mob Italy:</th><td>+39 347 520 8163</td></tr>
      </table>
    </div>

    <div class="band band--bottom"></div>
  </section>

  <section class="card card--back" aria-label="Business card back">
    <div class="back-panel">
      <span class="brand-mark"></span>
      <span class="brand-name">Brume Analytica</span>
    </div>
  </section>
</main>
</body>
</html>
```